Peanut Butter for Dogs - Label

Dear Designers,

Our company develops natural & innovative products aimed at enhancing animal (cat & dog) well-being. The company focuses on producing high-end, ethically sourced products that naturally soothe pets, improving their quality of life.

We are currently developing a new CBD-enriched Peanut Butter product for dogs, and we are looking for some label designs that follow our brand image & brand identity.

-> Please see full brief PDF file attached.

Target Market(s)

European Market (French Speaking)

Industry/Entity Type

Pet Food

Font styles to use
Other font styles liked:
• Please see brand kit in PDF brief

Colors

Designer to choose colors to be used in the design.

Requirements
Must have
• Please see brief PDF file attached
Nice to have
Should not have

```html
<!DOCTYPE html>
<html lang="fr">
<head>
<meta charset="utf-8">
<title>Tendresse Apaisante – Étiquette</title>
<link rel="stylesheet" href="https://fonts.googleapis.com/css2?family=Quicksand:wght@500;600;700&family=Roboto+Slab:wght@500;600&display=swap">
<style>
  :root {
    --backdrop: #f8f0e4;
    --label: #ffffff;
    --teal: #3aa58a;
    --teal-soft: #55b89c;
    --forest: #2f4a3b;
    --ink: #3a3a3a;
    --photo-a: #e9e4e2;
    --photo-b: #cfc5c2;
  }
  * { margin: 0; padding: 0; box-sizing: border-box; }
  html, body { width: 1198px; height: 1200px; overflow: hidden; }
  body { background: var(--backdrop); font-family: "Quicksand", sans-serif; position: relative; }

  .label {
    position: absolute; left: 40px; top: 260px;
    width: 1118px; height: 680px;
    background: var(--label);
    overflow: hidden;
    box-shadow: 0 2px 14px rgba(0,0,0,0.06);
  }
  .brand {
    position: absolute; top: 118px; left: 0; width: 100%;
    text-align: center; color: var(--forest);
  }
  .brand-name {
    font-family: "Roboto Slab", serif; font-weight: 600;
    font-size: 60px; letter-spacing: 2px; line-height: 1;
  }
  .brand-tag {
    font-family: "Roboto Slab", serif; font-weight: 600;
    font-size: 20px; color: var(--teal); line-height: 1;
    margin-top: 8px; margin-left: 190px;
  }
  .divider { position: absolute; left: 0; top: 200px; }

  .title { position: absolute; left: 62px; top: 300px; }
  .title-main {
    font-weight: 700; font-size: 74px; color: var(--teal);
    line-height: 1; letter-spacing: 0.5px;
  }
  .title-sub {
    font-weight: 700; font-size: 40px; color: var(--teal);
    line-height: 1.2; margin-top: 8px;
  }
  .dose {
    font-weight: 500; font-size: 31px; color: var(--ink);
    margin-left: 146px; margin-top: 2px;
  }

  .features {
    position: absolute; left: 62px; top: 535px;
    display: grid; grid-template-columns: 200px 300px; row-gap: 26px;
  }
  .feature { display: flex; align-items: center; gap: 12px; font-size: 23px; font-weight: 500; color: var(--ink); }
  .feature svg { flex: none; }

  .photo {
    position: absolute; left: 612px; top: 258px;
    width: 560px; height: 560px; border-radius: 50%;
    border: 5px solid var(--teal-soft);
    background: radial-gradient(circle at 45% 45%, var(--photo-a), var(--photo-b));
  }
</style>
</head>
<body>
  <div class="label">
    <div class="brand">
      <div class="brand-name">VERDALIS</div>
      <div class="brand-tag">For Animals</div>
    </div>

    <svg class="divider" width="1118" height="100" viewBox="0 0 1118 100" aria-hidden="true">
      <polyline points="0,22 518,22 559,66 600,22 1118,22" fill="none" stroke="var(--teal)" stroke-width="4" stroke-linejoin="round"/>
    </svg>

    <div class="title">
      <div class="title-main">TENDRESSE</div>
      <div class="title-sub">Apaisante</div>
      <div class="dose">CBD 150 MG</div>
    </div>

    <div class="features">
      <div class="feature">
        <svg width="32" height="32" viewBox="0 0 32 32"><circle cx="16" cy="16" r="14" fill="none" stroke="var(--forest)" stroke-width="1.6"/><circle cx="16" cy="11" r="3" fill="var(--teal)"/><circle cx="11" cy="20" r="3" fill="var(--teal)"/><circle cx="21" cy="20" r="3" fill="var(--teal)"/></svg>
        <span>Anti-Stress</span>
      </div>
      <div class="feature">
        <svg width="40" height="40" viewBox="0 0 40 40"><circle cx="20" cy="20" r="18" fill="none" stroke="var(--forest)" stroke-width="1.6"/><path d="M13 24 L20 14 L27 24" fill="none" stroke="var(--teal)" stroke-width="2.4" stroke-linecap="round" stroke-linejoin="round" transform="rotate(180 20 19)"/></svg>
        <span>100% naturel</span>
      </div>
      <div class="feature">
        <svg width="32" height="32" viewBox="0 0 32 32"><circle cx="16" cy="16" r="14" fill="none" stroke="var(--forest)" stroke-width="1.6"/><path d="M10 13 Q16 22 22 13" fill="none" stroke="var(--teal)" stroke-width="2.2" stroke-linecap="round"/></svg>
        <span>A lécher</span>
      </div>
      <div class="feature">
        <svg width="40" height="40" viewBox="0 0 40 40"><circle cx="20" cy="20" r="18" fill="none" stroke="var(--forest)" stroke-width="1.6"/><rect x="12" y="14" width="16" height="14" rx="3" fill="var(--teal)"/></svg>
        <span>Beurre de cacahuète</span>
      </div>
    </div>

    <div class="photo" role="img" aria-label="Photo d'un chien au pelage clair léchant du beurre de cacahuète"></div>
  </div>
</body>
</html>
```